Travel Company is looking for a STAND OUT Business Card

I need a unique Business Card that will truly stand out. Nothing too busy. Simple is good, right? Not looking for a standard design either. No cookie cutter layout. We are a Travel Company that works more with Companies than Travelers. I had an idea to focus and emphasis on the 2 logo a bit more. This is not necessary, however thought it would look interesting. I am just looking for something interesting and a bit different. Does't have to completely off the wall crazy, just not your run of the mill business card.

Target Market(s)

Hoteliers, Resort Management, Call Centers, Executives, Travelers, Families, Businesses

Industry/Entity Type

Hospitality

Contact Information for Business Card

President/CEO - Marcus T Bellamy (title not necessary if design doesn't allow for it)
contact - (407) 555-0186
email - mbellamy@wayfarenow.example
address - 4812 Quillmore Ave #164
Orlando, FL 32804
website - www.wayfarenow.example

Font styles to use
Serif
Other font styles liked:
• Avenir Next LT Pro BOLD

Requirements
Must have
• simple look and design. Unique design
Nice to have
• I attached the 2 logo separate from the main logo. This can be used separately from the Main Logo, together with the main logo or as main logo. I included the logo font. Use it or not, designers choice.
Should not have
• cookie cutter design. Little use of red other than the logo

```html
<!DOCTYPE html>
<html lang="en">
<head>
<meta charset="utf-8">
<title>Wayfare Now – Business Card</title>
<link href="https://fonts.googleapis.com/css2?family=Open+Sans:wght@400;600;700;800&family=Roboto:wght@400&display=swap" rel="stylesheet">
<style>
  :root {
    --backdrop: #e6e5e5;
    --card-dark: #1e1f21;
    --card-light: #f7f7f7;
    --accent-red: #d9262a;
    --ink: #1f1f1f;
    --ink-soft: #333333;
    --white: #ffffff;
    --watermark: #eeeae8;
  }
  * { margin: 0; padding: 0; box-sizing: border-box; }
  html, body {
    width: 1200px; height: 1200px; overflow: hidden;
    background: var(--backdrop);
  }
  .canvas { position: relative; width: 1200px; height: 1200px; }

  .card { position: absolute; width: 713px; height: 420px; overflow: hidden; }

  /* Front */
  .card-front { left: 238px; top: 117px; background: var(--card-dark); }
  .card-front .accent-band {
    position: absolute; left: 0; right: 0; bottom: 0; height: 9px;
    background: var(--accent-red);
  }
  .brand {
    position: absolute; display: flex; align-items: center; gap: 10px;
    font-family: "Open Sans", sans-serif; font-weight: 800;
    letter-spacing: -1px; white-space: nowrap;
  }
  .brand-dot { width: 16px; height: 16px; border-radius: 50%; background: var(--accent-red); flex: none; }
  .card-front .brand {
    left: 0; right: 0; top: 125px; justify-content: center;
    font-size: 50px; color: var(--white);
  }
  .card-front .website {
    position: absolute; left: 0; right: 0; top: 338px; text-align: center;
    font-family: "Open Sans", sans-serif; font-size: 18px; font-weight: 400;
    letter-spacing: 1.2px; color: var(--white);
  }

  /* Back */
  .card-back { left: 230px; top: 644px; height: 417px; background: var(--card-light); }
  .watermark-ring {
    position: absolute; left: 470px; top: 40px; width: 300px; height: 300px;
    border: 18px solid var(--watermark); border-radius: 50%;
  }
  .card-back .brand {
    left: 88px; top: 166px; font-size: 40px; color: var(--ink);
  }
  .contact-block {
    position: absolute; left: 415px; top: 100px;
    font-family: "Roboto", sans-serif; color: var(--ink-soft);
  }
  .contact-name {
    font-family: "Open Sans", sans-serif; font-weight: 700; font-size: 25px;
    color: var(--ink); line-height: 34px;
  }
  .contact-title {
    font-family: "Open Sans", sans-serif; font-size: 15px; line-height: 20px;
    color: var(--ink-soft); margin-bottom: 30px; letter-spacing: 0.3px;
  }
  .contact-list { list-style: none; }
  .contact-list li {
    display: flex; align-items: center; gap: 14px;
    font-size: 18px; line-height: 25.5px;
  }
  .contact-list svg { width: 18px; height: 14px; flex: none; fill: var(--accent-red); }
  .address { font-size: 18px; line-height: 26px; margin-top: 2px; }
</style>
</head>
<body>
<div class="canvas">

  <section class="card card-front">
    <div class="brand"><span class="brand-dot"></span>wayfare now</div>
    <p class="website">www.wayfarenow.example</p>
    <div class="accent-band"></div>
  </section>

  <section class="card card-back">
    <div class="watermark-ring"></div>
    <div class="brand"><span class="brand-dot"></span>wayfare now</div>

    <div class="contact-block">
      <h1 class="contact-name">Marcus T Bellamy</h1>
      <p class="contact-title">President/CEO</p>
      <ul class="contact-list">
        <li>
          <svg viewBox="0 0 18 14" aria-hidden="true"><path d="M1 5c0-3 4-4 8-4s8 1 8 4l-3 1-1-2H5L4 6zM4 7h10l2 6H2z"/></svg>
          (407) 555-0186
        </li>
        <li>
          <svg viewBox="0 0 18 14" aria-hidden="true"><path d="M9 0a7 7 0 1 0 0 14A7 7 0 0 0 9 0zm0 1.4c.9 0 1.9 1.9 2.2 4.6H6.8C7.1 3.3 8.1 1.4 9 1.4zM3.4 6h2c.1-1.5.4-2.9 1-3.8A5.6 5.6 0 0 0 3.4 6zm9.2 0h2a5.6 5.6 0 0 0-3-3.8c.6.9.9 2.3 1 3.8zM3.4 8a5.6 5.6 0 0 0 3 3.8c-.6-.9-.9-2.3-1-3.8zm3.4 0c.3 2.7 1.3 4.6 2.2 4.6s1.9-1.9 2.2-4.6zm5.8 0c-.1 1.5-.4 2.9-1 3.8a5.6 5.6 0 0 0 3-3.8z"/></svg>
          www.wayfarenow.example
        </li>
        <li>
          <svg viewBox="0 0 18 14" aria-hidden="true"><path d="M1 1h16v1.5L9 8 1 2.5zm0 3.3 8 5.5 8-5.5V13H1z"/></svg>
          mbellamy@wayfarenow.example
        </li>
      </ul>
      <p class="address">4812 Quillmore Ave #164<br>Orlando, FL 32804</p>
    </div>
  </section>

</div>
</body>
</html>
```